Label Design for Saffron Company

We need a label design that is unique for our container. The item inside the container is Saffron, and it is 5g in weigh. We need on the label our logo, the weight and quality. Here is the exactly what we want. We want the background to be black for the label and the design to present royalty, and premium quality.

Premium Quality
Grade A+ Premium Saffron
100% Natural and Pure
www.QamarivaSpice.com

Target Market(s)

Everyone

Requirements
Must have
• Black background, golden border design. Unique design, that show premium and royalty.
Nice to have
• The logo is attached with transparent background so you can show exactly how things look like.
Should not have
• different colors that are not part of the logo.

```html
<!DOCTYPE html>
<html lang="en">
<head>
<meta charset="utf-8">
<title>Qamariva Spice – Saffron Labels</title>
<link rel="stylesheet" href="https://fonts.googleapis.com/css2?family=Marcellus&family=Montserrat:wght@400;600;700&display=swap">
<style>
  :root {
    --stage: #6b6b6e;
    --label-black: #15171c;
    --label-black-deep: #0e0f13;
    --gold: #cfa94f;
    --gold-soft: #b8933f;
    --ivory: #eeeae2;
    --white: #f4f4f4;
  }
  * { margin: 0; padding: 0; box-sizing: border-box; }
  html, body {
    width: 1200px;
    height: 937px;
    overflow: hidden;
    background: var(--stage);
  }
  .canvas {
    position: relative;
    width: 1200px;
    height: 937px;
  }
  .lid-label {
    position: absolute;
    left: 143px;
    top: 437px;
    width: 362px;
    height: 362px;
  }
  .box-label {
    position: absolute;
    left: 583px;
    top: 431px;
    width: 540px;
    height: 430px;
  }
  .brand-top {
    font-family: "Marcellus", serif;
    fill: var(--ivory);
    letter-spacing: 0.22em;
  }
  .brand-bottom {
    font-family: "Marcellus", serif;
    fill: var(--ivory);
    letter-spacing: 0.08em;
  }
  .kicker {
    font-family: "Montserrat", sans-serif;
    font-weight: 400;
    fill: var(--white);
    letter-spacing: 0.35em;
  }
  .grade {
    font-family: "Montserrat", sans-serif;
    font-weight: 700;
    fill: var(--white);
    letter-spacing: 0.25em;
  }
  .headline {
    font-family: "Montserrat", sans-serif;
    font-weight: 600;
    fill: var(--gold);
  }
  .purity {
    font-family: "Montserrat", sans-serif;
    font-weight: 400;
    fill: var(--white);
    letter-spacing: 0.38em;
  }
  .weight {
    font-family: "Montserrat", sans-serif;
    font-weight: 600;
    fill: var(--gold);
  }
  .web {
    font-family: "Montserrat", sans-serif;
    font-weight: 400;
    fill: var(--white);
    letter-spacing: 0.2em;
  }
  .frame-line { fill: none; stroke: var(--gold-soft); stroke-width: 1; }
  .mark-square { fill: none; stroke: var(--gold); stroke-width: 1.6; }
</style>
</head>
<body>
<main class="canvas">

  <!-- Round lid label -->
  <svg class="lid-label" viewBox="0 0 400 400" aria-label="Round lid label">
    <defs>
      <radialGradient id="lidFill" cx="50%" cy="40%" r="60%">
        <stop offset="0" stop-color="#1c1e24"/>
        <stop offset="1" stop-color="#111217"/>
      </radialGradient>
      <path id="lidTopArc" d="M 34 200 A 166 166 0 0 1 366 200"/>
      <path id="lidBottomArc" d="M 24 200 A 176 176 0 0 0 376 200"/>
    </defs>
    <circle cx="200" cy="200" r="198" fill="url(#lidFill)"/>
    <path class="frame-line" d="M 267.6 55 A 160 160 0 0 1 291.8 331.1"/>
    <path class="frame-line" d="M 108.2 331.1 A 160 160 0 0 1 132.4 55"/>
    <text class="kicker" font-size="10.5"><textPath href="#lidTopArc" startOffset="50%" text-anchor="middle">PREMIUM QUALITY</textPath></text>
    <text class="web" font-size="9.5" letter-spacing="1.6"><textPath href="#lidBottomArc" startOffset="50%" text-anchor="middle">WWW.QAMARIVASPICE.COM</textPath></text>

    <rect class="mark-square" x="166" y="58" width="68" height="66"/>
    <text class="brand-top" x="200" y="151" font-size="19" text-anchor="middle">QAMARIVA</text>
    <text class="brand-bottom" x="200" y="184" font-size="30" text-anchor="middle">SPICE</text>

    <text class="grade" x="200" y="224" font-size="11.5" text-anchor="middle">GRADE A+</text>
    <text class="headline" x="200" y="260" font-size="27" text-anchor="middle">PREMIUM SAFFRON</text>
    <text class="purity" x="200" y="281" font-size="9.5" text-anchor="middle">100% NATURAL AND PURE</text>
    <text class="weight" x="200" y="346" font-size="19" text-anchor="middle">5g</text>
  </svg>

  <!-- Box front label -->
  <svg class="box-label" viewBox="0 0 540 430" aria-label="Box front label">
    <defs>
      <linearGradient id="boxFill" x1="0" y1="0" x2="1" y2="1">
        <stop offset="0" stop-color="#181a1f"/>
        <stop offset="1" stop-color="#0e0f13"/>
      </linearGradient>
    </defs>
    <rect width="540" height="430" fill="url(#boxFill)"/>
    <path class="frame-line" d="M 155 19 H 22 V 411 H 128 M 413 411 H 518 V 19 H 385"/>

    <text class="kicker" x="270" y="23.5" font-size="12" text-anchor="middle">PREMIUM QUALITY</text>

    <rect class="mark-square" x="226" y="48" width="88" height="78"/>
    <text class="brand-top" x="270" y="156" font-size="22" text-anchor="middle">QAMARIVA</text>
    <text class="brand-bottom" x="270" y="190" font-size="34" text-anchor="middle">SPICE</text>

    <text class="grade" x="270" y="254" font-size="15" text-anchor="middle">GRADE A+</text>
    <text class="headline" x="270" y="294" font-size="40" text-anchor="middle">PREMIUM SAFFRON</text>
    <text class="purity" x="270" y="322" font-size="13.5" text-anchor="middle">100% NATURAL AND PURE</text>
    <text class="weight" x="270" y="382" font-size="22" text-anchor="middle">5g</text>
    <text class="web" x="270" y="415" font-size="11.5" text-anchor="middle">WWW.QAMARIVASPICE.COM</text>
  </svg>

</main>
</body>
</html>
```